Business Card Design Project

I am looking for a classy business card design for a product design consultancy. We specialize in Product Design, Prototyping, and Manufacturing Consulting. Products that we design range from consumer electronics to household products all the way to sporting goods. We are based in Arizona and called "Heron Design Works." We like to have fun and goof off as much as we like to create new products. We are young and energetic so we would like our business cards to reflect that. We already have a logo that we would like to implement into the card design. A plain rectangular business card is boring so feel free to get creative, but please, no avocado shaped cards (it's far too literal). Also feel free to play around with textured card stocks or plastic. The final design that we choose will pay attention to all of the little details. Our cards will need to be 2 sided. We're giving you guys free reign to design as you would like. Please have fun with this, it will reflect in our business card.

Thanks guys,
Heron Design Works Team

Industry/Entity Type

Electronics

Requirements
Must have
• We would like to have a spot UV coating somewhere on the business card design if possible.
Nice to have
• Let's see some designs with custom shapes rather than typical rectangular business cards but please no avocado shaped cards, thanks. Also play around with textured card socks.

```html
<!DOCTYPE html>
<html lang="en">
<head>
<meta charset="utf-8">
<title>Heron Design Works – Business Card</title>
<link rel="stylesheet" href="https://fonts.googleapis.com/css2?family=Questrial&display=swap">
<style>
  :root {
    --backdrop: #2a2a2a;
    --card: #1c1c1c;
    --lime: #8cd63a;
    --grey-text: #b9b9b9;
  }
  * { margin: 0; padding: 0; box-sizing: border-box; }
  html, body {
    width: 1200px;
    height: 900px;
    overflow: hidden;
    background: var(--backdrop);
    font-family: "Questrial", Arial, sans-serif;
  }
  .canvas {
    position: relative;
    width: 1200px;
    height: 900px;
  }
  .card {
    position: absolute;
    top: 300px;
    width: 525px;
    height: 300px;
    background: var(--card);
    overflow: hidden;
    box-shadow: 0 10px 30px rgba(0,0,0,0.45);
  }
  .card--front { left: 50px; }
  .card--back { left: 625px; }

  .pattern-area {
    position: absolute;
    left: 0;
    top: 0;
    width: 240px;
    height: 300px;
  }
  .pattern-area svg { display: block; width: 100%; height: 100%; }

  .brand {
    display: flex;
    align-items: center;
    gap: 8px;
    color: var(--lime);
    white-space: nowrap;
  }
  .brand__dot {
    width: 18px;
    height: 18px;
    border-radius: 50%;
    background: var(--lime);
    flex: none;
  }
  .brand__name {
    font-size: 26px;
    letter-spacing: 0.3px;
    line-height: 1;
  }

  .front-identity {
    position: absolute;
    right: 24px;
    top: 132px;
  }
  .front-web {
    margin-top: 14px;
    padding-left: 26px;
    font-size: 14px;
    color: var(--grey-text);
    letter-spacing: 0.3px;
    white-space: nowrap;
  }
  .accent { color: var(--lime); }

  .card--back .pattern-area { width: 200px; height: 210px; }
  .card--back .brand {
    position: absolute;
    right: 28px;
    top: 48px;
  }
  .contact {
    position: absolute;
    right: 28px;
    top: 122px;
    text-align: right;
    color: var(--grey-text);
    font-size: 15px;
    line-height: 1.35;
    white-space: nowrap;
  }
  .contact__name {
    color: var(--lime);
    font-size: 17px;
    letter-spacing: 0.6px;
    text-transform: uppercase;
  }
  .contact__role { margin-bottom: 10px; }
  .contact__phone { color: var(--lime); letter-spacing: 0.5px; }
</style>
</head>
<body>
<main class="canvas">

  <section class="card card--front" aria-label="Business card front">
    <div class="pattern-area" role="img" aria-label="Repeating pattern of the brand symbol in lime green on black">
      <svg viewBox="0 0 240 300" preserveAspectRatio="none">
        <defs>
          <linearGradient id="front-pattern" x1="0" y1="0" x2="1" y2="1">
            <stop offset="0" stop-color="#7cc233"/>
            <stop offset="1" stop-color="#8cd63a"/>
          </linearGradient>
        </defs>
        <path d="M0 0 H150 L175 40 L180 90 L195 140 L205 190 L215 240 L225 300 H0 Z" fill="url(#front-pattern)"/>
      </svg>
    </div>
    <div class="front-identity">
      <div class="brand">
        <span class="brand__dot"></span>
        <span class="brand__name">Heron Design Works</span>
      </div>
      <p class="front-web">www.<span class="accent">heron</span>designworks.com</p>
    </div>
  </section>

  <section class="card card--back" aria-label="Business card back">
    <div class="pattern-area" role="img" aria-label="Faint spot UV pattern of the brand symbol, dark on black">
      <svg viewBox="0 0 200 210" preserveAspectRatio="none">
        <defs>
          <linearGradient id="back-pattern" x1="0" y1="0" x2="1" y2="1">
            <stop offset="0" stop-color="#242424"/>
            <stop offset="1" stop-color="#1f1f1f"/>
          </linearGradient>
        </defs>
        <path d="M0 0 H200 L170 50 L140 100 L110 150 L80 210 H0 Z" fill="url(#back-pattern)"/>
      </svg>
    </div>
    <div class="brand">
      <span class="brand__dot"></span>
      <span class="brand__name">Heron Design Works</span>
    </div>
    <div class="contact">
      <p class="contact__name">Lena Marlow</p>
      <p class="contact__role">Sales Manager</p>
      <p class="contact__phone">+ 123 555 0148</p>
      <p><span class="accent">info</span>@herondesignworks.com</p>
      <p>www.<span class="accent">heron</span>designworks.com</p>
    </div>
  </section>

</main>
</body>
</html>
```